Price List Modified

We have a price list in PDF that we need changed. The current price list is in Euro's and we need the Euro's changed to U.S. dollars. We simply use a conversion factor of 1.55 for this.

We also need the dimensions of units converted from MM to inches.

Industry/Entity Type

Graphic Design

```html
<!DOCTYPE html>
<html lang="en">
<head>
<meta charset="utf-8">
<title>RHT Regeneration and Holding Trolleys – Price List</title>
<link rel="stylesheet" href="https://fonts.googleapis.com/css2?family=Roboto+Condensed:wght@300;400;700&display=swap">
<style>
:root{
  --ink:#1a1a1a;
  --muted:#444;
  --accent:#f08a24;
  --rule:#c9c9c9;
  --gold:#d8b56a;
  --steel-light:#c9cacb;
  --steel-dark:#8c8e90;
  --paper:#ffffff;
}
*{box-sizing:border-box;margin:0;padding:0}
html,body{width:849px;height:1200px;overflow:hidden;background:var(--paper)}
body{position:relative;font-family:"Roboto Condensed",Arial,sans-serif;color:var(--ink)}
.abs{position:absolute}
.page-title{left:50px;top:46px;font-size:13px;line-height:17px}
.page-title .it{font-weight:700}
.page-title .en{font-weight:400}
.category-icon{left:740px;top:48px;width:60px;height:50px}
.power-icon{left:50px;top:118px;width:16px;height:15px}
.series-title{left:228px;top:110px;font-size:26px;line-height:30px}
.series-title b{font-weight:700}
.series-title span{font-weight:300;font-size:22px}
.series-rule{left:50px;top:139px;width:750px;height:5px;background:var(--accent)}
.head{top:148px;font-size:9.5px;line-height:11px;color:var(--ink)}
.head small{display:block;color:var(--muted);font-size:9.5px;font-weight:300}
.col-sep{width:1px;background:var(--rule)}
.cell{font-size:8.5px;line-height:10.5px;color:var(--ink)}
.code{font-size:11px;font-weight:700}
.cap b{font-size:11px}
.price{font-weight:700}
.row-rule{height:1px;background:var(--rule);left:228px;width:572px}
.product-photo{background:linear-gradient(90deg,var(--steel-dark),var(--steel-light) 45%,var(--steel-dark));border-radius:3px}
.photo-label{font-size:9px}
.note{font-size:9.5px;line-height:11.5px}
.note .en{font-weight:300}
.tank-icon{width:34px;height:34px}
.footer-rule{left:50px;top:1150px;width:750px;height:1px;background:var(--gold)}
.page-num{left:50px;top:1166px;font-size:15px}
</style>
</head>
<body>

<header>
  <div class="abs page-title">
    <div class="it">CARRELLI DI RIMESSA IN TEMPERATURA E MANTENIMENTO +3°C &nbsp;⟶ +65°C</div>
    <div class="en">REGENERATION AND HOLDING TROLLEYS +3°C &nbsp;⟶ +65°C</div>
  </div>
  <svg class="abs category-icon" viewBox="0 0 60 50" aria-label="Hot food category">
    <rect width="60" height="50" rx="5" fill="var(--accent)"/>
    <path d="M16 33 h28 a14 6 0 0 1 -28 0z" fill="none" stroke="#fff" stroke-width="2"/>
    <path d="M12 38 h36" stroke="#fff" stroke-width="2"/>
    <path d="M25 28 q-3-4 0-8 q3-4 0-8 M30 28 q-3-4 0-8 q3-4 0-8 M35 28 q-3-4 0-8 q3-4 0-8" fill="none" stroke="#fff" stroke-width="1.6"/>
  </svg>
  <svg class="abs power-icon" viewBox="0 0 16 15" aria-label="Electric">
    <rect width="16" height="15" fill="var(--ink)"/>
    <path d="M9 2 L5 8 H8 L6 13 L11 6 H8z" fill="#fff"/>
  </svg>
</header>

<section class="series">
  <h1 class="abs series-title"><b>RHT</b> <span>- 161 - 162</span></h1>
  <div class="abs series-rule"></div>

  <div class="abs head" style="left:233px">Codice<small>Code</small></div>
  <div class="abs head" style="left:293px">Versione<small>Version</small></div>
  <div class="abs head" style="left:385px">Capacità<small>Capacity</small></div>
  <div class="abs head" style="left:459px">Passo guide<small>Distance guides</small></div>
  <div class="abs head" style="left:528px">Dimensioni inch<small>Dimensions inch</small></div>
  <div class="abs head" style="left:609px">Peso<small>Weight</small></div>
  <div class="abs head" style="left:653px">Power V/50Hz</div>
  <div class="abs head" style="left:745px">$</div>
  <div class="abs col-sep" style="left:288px;top:146px;height:28px"></div>
  <div class="abs col-sep" style="left:380px;top:146px;height:28px"></div>
  <div class="abs col-sep" style="left:454px;top:146px;height:28px"></div>
  <div class="abs col-sep" style="left:523px;top:146px;height:28px"></div>
  <div class="abs col-sep" style="left:604px;top:146px;height:28px"></div>
  <div class="abs col-sep" style="left:648px;top:146px;height:28px"></div>
  <div class="abs col-sep" style="left:738px;top:146px;height:28px"></div>

  <!-- Group 153 -->
  <div class="abs product-photo" role="img" aria-label="Stainless steel two-door holding trolley with electronic control panel" style="left:48px;top:200px;width:114px;height:190px"></div>
  <div class="abs photo-label" style="left:48px;top:400px">RHT 153 E</div>

  <div class="abs col-sep" style="left:288px;top:200px;height:102px"></div>
  <div class="abs col-sep" style="left:380px;top:200px;height:102px"></div>
  <div class="abs col-sep" style="left:454px;top:200px;height:102px"></div>
  <div class="abs col-sep" style="left:523px;top:200px;height:102px"></div>
  <div class="abs col-sep" style="left:604px;top:200px;height:102px"></div>
  <div class="abs col-sep" style="left:648px;top:200px;height:102px"></div>
  <div class="abs col-sep" style="left:738px;top:200px;height:102px"></div>

  <div class="abs cell code" style="left:232px;top:222px">RHT 153 M</div>
  <div class="abs cell" style="left:293px;top:206px">Elettromeccanica<br>con umidificatore<br><span style="font-weight:300">Electromechanical<br>with humidity</span></div>
  <div class="abs cell cap" style="left:387px;top:215px"><b>16</b> GN 2/1<br><b>32</b> GN 1/1</div>
  <div class="abs cell" style="left:460px;top:224px">2.8 inch</div>
  <svg class="abs" style="left:494px;top:218px" width="16" height="22" viewBox="0 0 16 22"><path d="M8 2v18M4 6l4-4 4 4M4 16l4 4 4-4M1 1h4M11 21h4" fill="none" stroke="#333" stroke-width="1"/></svg>
  <div class="abs cell" style="left:528px;top:224px">39.6x33x66 h</div>
  <div class="abs cell" style="left:609px;top:224px">143 Kg</div>
  <div class="abs cell" style="left:653px;top:224px">kW 9,6 3N AC 400V</div>
  <div class="abs cell price" style="left:745px;top:224px">9,842.50</div>
  <div class="abs row-rule" style="top:254px"></div>

  <div class="abs cell code" style="left:232px;top:273px">RHT 153 E</div>
  <div class="abs cell" style="left:293px;top:263px">Elettronica con<br>umidificatore<br><span style="font-weight:300">Electronic with humidity</span></div>
  <div class="abs cell cap" style="left:387px;top:268px"><b>16</b> GN 2/1<br><b>32</b> GN 1/1</div>
  <div class="abs cell" style="left:460px;top:274px">2.8 inch</div>
  <svg class="abs" style="left:494px;top:267px" width="16" height="22" viewBox="0 0 16 22"><path d="M8 2v18M4 6l4-4 4 4M4 16l4 4 4-4M1 1h4M11 21h4" fill="none" stroke="#333" stroke-width="1"/></svg>
  <div class="abs cell" style="left:528px;top:274px">39.6x33x66 h</div>
  <div class="abs cell" style="left:609px;top:274px">143 Kg</div>
  <div class="abs cell" style="left:653px;top:274px">kW 9,6 3N AC 400V</div>
  <div class="abs cell price" style="left:745px;top:274px">10,695.00</div>
  <div class="abs row-rule" style="top:302px"></div>

  <div class="abs note" style="left:228px;top:315px">Completi di paratie portateglie GN 1/1<br><span class="en">Supplied with guide rails GN 1/1</span></div>
  <svg class="abs tank-icon" style="left:229px;top:350px" viewBox="0 0 34 34" aria-label="Drain tank"><circle cx="17" cy="17" r="16" fill="none" stroke="#555"/><rect x="9" y="11" width="16" height="10" fill="none" stroke="#555" transform="rotate(-20 17 16)"/><path d="M6 28 L28 6" stroke="#555"/></svg>
  <div class="abs note" style="left:275px;top:352px">Serbatoio riserve d'acqua a scomparsa<br><span class="en">Inbuild drain storage tank</span></div>

  <!-- Group 162 -->
  <div class="abs product-photo" role="img" aria-label="Stainless steel two-door holding trolley with top control panel" style="left:48px;top:430px;width:112px;height:215px"></div>
  <div class="abs photo-label" style="left:48px;top:655px">RHT 162 E</div>

  <div class="abs col-sep" style="left:288px;top:430px;height:130px"></div>
  <div class="abs col-sep" style="left:380px;top:430px;height:130px"></div>
  <div class="abs col-sep" style="left:454px;top:430px;height:130px"></div>
  <div class="abs col-sep" style="left:523px;top:430px;height:130px"></div>
  <div class="abs col-sep" style="left:604px;top:430px;height:130px"></div>
  <div class="abs col-sep" style="left:648px;top:430px;height:130px"></div>
  <div class="abs col-sep" style="left:738px;top:430px;height:130px"></div>

  <div class="abs cell code" style="left:232px;top:458px">RHT 162 M</div>
  <div class="abs cell" style="left:293px;top:442px">Elettromeccanica<br>con umidificatore<br><span style="font-weight:300">Electromechanical<br>with humidity</span></div>
  <div class="abs cell cap" style="left:387px;top:459px"><b>16</b> GN 2/1</div>
  <div class="abs cell" style="left:460px;top:460px">3.2 inch</div>
  <svg class="abs" style="left:494px;top:454px" width="16" height="22" viewBox="0 0 16 22"><path d="M8 2v18M4 6l4-4 4 4M4 16l4 4 4-4M1 1h4M11 21h4" fill="none" stroke="#333" stroke-width="1"/></svg>
  <div class="abs cell" style="left:528px;top:460px">38x37.4x74 h</div>
  <div class="abs cell" style="left:609px;top:460px">170 Kg</div>
  <div class="abs cell" style="left:653px;top:460px">kW 9,6 3N AC 400V</div>
  <div class="abs cell price" style="left:745px;top:460px">9,300.00</div>
  <div class="abs row-rule" style="top:496px"></div>

  <div class="abs cell code" style="left:232px;top:522px">RHT 162 E</div>
  <div class="abs cell" style="left:293px;top:506px">Elettronica con<br>umidificatore<br><span style="font-weight:300">Electronic with<br>humidity</span></div>
  <div class="abs cell cap" style="left:387px;top:523px"><b>16</b> GN 2/1</div>
  <div class="abs cell" style="left:460px;top:524px">3.2 inch</div>
  <svg class="abs" style="left:494px;top:518px" width="16" height="22" viewBox="0 0 16 22"><path d="M8 2v18M4 6l4-4 4 4M4 16l4 4 4-4M1 1h4M11 21h4" fill="none" stroke="#333" stroke-width="1"/></svg>
  <div class="abs cell" style="left:528px;top:524px">38x37.4x74 h</div>
  <div class="abs cell" style="left:609px;top:524px">170 Kg</div>
  <div class="abs cell" style="left:653px;top:524px">kW 9,6 3N AC 400V</div>
  <div class="abs cell price" style="left:745px;top:524px">10,152.50</div>
  <div class="abs row-rule" style="top:560px"></div>

  <div class="abs note" style="left:228px;top:575px">Completo di paratie portateglie GN 2/1<br><span class="en">Supplied with guide rails GN 2/1</span></div>
  <svg class="abs tank-icon" style="left:229px;top:619px" viewBox="0 0 34 34" aria-label="Drain tank"><circle cx="17" cy="17" r="16" fill="none" stroke="#555"/><rect x="9" y="11" width="16" height="10" fill="none" stroke="#555" transform="rotate(-20 17 16)"/><path d="M6 28 L28 6" stroke="#555"/></svg>
  <div class="abs note" style="left:275px;top:621px">Serbatoio riserve d'acqua a scomparsa<br><span class="en">Inbuild drain storage tank</span></div>
</section>

<footer>
  <div class="abs footer-rule"></div>
  <div class="abs page-num">34</div>
</footer>

</body>
</html>
```